UK Online Escort Directory Requires a Redesigned Email Marketing Campaign (4 emails total)

These emails should be designed as marketing emails that will be sent out to approx 10,000 potential customers on a by monthly basis. The designs should be innovative, professional designs that are capable of capturing a readers attention in the blink of an eye.

We have posted this job as our in-house design capabilities are not able to create professional email designs, we therefore require a designer to redesign our email marketing campaign (4 emails total) to a professional level.

The content of the emails will be provided, along with the 5 emails that we are currently sending and the company logo. This should give the potential designer all that they need to redesign the campaign to a professional level.

Please see attached brief for more information on what is required from each individual email.

Target Market(s)

Escorts throughout the UK

Industry/Entity Type

Escort

Font styles to use
Serif
Sans Serif

Requirements
Must have
• Instant recognition of what's being offered.
Nice to have
• Imaginative / inspirational designs.
Should not have
• Any unnecessary wording or text.

```html
<!DOCTYPE html>
<html lang="en">
<head>
<meta charset="utf-8">
<title>Velvet Listings – Welcome Email</title>
<link rel="stylesheet" href="https://fonts.googleapis.com/css2?family=Montserrat:wght@700&family=Open+Sans:ital,wght@0,300;0,400;0,600;0,700;1,400;1,700&display=swap">
<style>
  :root {
    --page-bg: #ffffff;
    --frame-blue: #cfe6fb;
    --panel-blue: #cce6fc;
    --card-yellow: #faf5bf;
    --ink: #1c1c1c;
    --accent-pink: #e3086a;
    --accent-purple: #a0428f;
    --button-blue: #0a80cc;
    --brand-blue: #6a86c8;
    --muted: #9a9a9a;
    --link: #2a6fc0;
    --photo-warm: #d9b894;
    --photo-light: #efe2cf;
  }
  * { box-sizing: border-box; margin: 0; padding: 0; }
  html, body {
    width: 971px; height: 1200px; overflow: hidden;
    background: var(--page-bg);
    font-family: "Open Sans", Arial, sans-serif;
    color: var(--ink);
  }
  .email { position: relative; width: 971px; height: 1200px; }

  .brand { position: absolute; left: 231px; top: 62px; width: 510px; }
  .brand-name {
    font-weight: 300; font-size: 50px; line-height: 60px;
    color: var(--accent-pink); letter-spacing: 0.5px;
  }
  .brand-tagline {
    font-weight: 600; font-size: 13px; color: var(--brand-blue);
    margin-left: 4px; margin-top: -2px;
  }

  .frame {
    position: absolute; left: 159px; top: 165px; width: 652px; height: 879px;
    border: 7px solid var(--frame-blue); background: #fff;
  }
  .panel {
    position: absolute; left: 182px; top: 191px; width: 607px; height: 824px;
    background: var(--panel-blue); border-radius: 5px;
  }

  .welcome-title {
    position: absolute; left: 182px; width: 607px; top: 228px;
    text-align: center; font-family: "Montserrat", Arial, sans-serif;
    font-weight: 700; font-size: 36px; letter-spacing: 4px; color: var(--ink);
  }
  .divider-dots {
    position: absolute; left: 440px; top: 306px; display: flex; gap: 19px;
  }
  .divider-dots span {
    width: 7px; height: 7px; border-radius: 50%; background: var(--accent-pink);
  }
  .stats {
    position: absolute; left: 182px; width: 607px; top: 349px;
    text-align: center; font-size: 22px; line-height: 29px;
  }
  .stats em { font-weight: 700; }

  .listing {
    position: absolute; left: 182px; top: 443px; width: 607px; height: 318px;
    background: var(--card-yellow);
  }
  .rating {
    position: absolute; right: 32px; top: 11px; display: flex; align-items: center; gap: 4px;
    font-family: "Montserrat", Arial, sans-serif; font-weight: 700; font-size: 15px;
    color: var(--accent-purple);
  }
  .rating-label { margin-right: 4px; }
  .rating svg { width: 16px; height: 16px; fill: var(--accent-purple); }
  .listing-photo {
    position: absolute; left: 34px; top: 40px; width: 168px; height: 245px;
    border: 6px solid #fff; border-radius: 12px;
    background: linear-gradient(160deg, var(--photo-light), var(--photo-warm) 60%, #8a6e6a);
    box-shadow: 0 1px 3px rgba(0,0,0,0.15);
  }
  .listing-info { position: absolute; left: 232px; top: 53px; width: 340px; }
  .listing-name { font-weight: 700; font-size: 21px; line-height: 25px; }
  .listing-area { font-weight: 700; font-size: 17px; line-height: 20px; }
  .listing-text { margin-top: 16px; font-size: 17.5px; line-height: 30px; }

  .cta {
    position: absolute; height: 51px; border-radius: 3px; color: #fff;
    display: flex; align-items: center; justify-content: center; gap: 20px;
    font-size: 18px; text-decoration: none;
  }
  .cta strong { font-weight: 700; }
  .cta-browse { left: 255px; top: 817px; width: 479px; background: var(--accent-pink); }
  .cta-post { left: 256px; top: 909px; width: 480px; background: var(--button-blue); gap: 9px; }

  .footer {
    position: absolute; left: 0; width: 971px; top: 1067px; text-align: center;
    font-style: italic; font-size: 14.5px; color: var(--muted);
  }
  .footer a { color: var(--link); }
</style>
</head>
<body>
<main class="email">
  <header class="brand">
    <div class="brand-name">velvetlistings-uk.com</div>
    <div class="brand-tagline">The Escort Directory</div>
  </header>

  <div class="frame"></div>
  <div class="panel"></div>

  <h1 class="welcome-title">Welcome</h1>
  <div class="divider-dots"><span></span><span></span><span></span><span></span></div>
  <p class="stats">Last week this ad was <em>viewed 963 times</em> and<br><em>produced 150 phone calls</em> for just <em>£40.49 pm</em>.</p>

  <section class="listing">
    <div class="rating">
      <span class="rating-label">Recommended</span>
      <svg viewBox="0 0 24 24"><path d="M12 2l2.9 6.9 7.1.6-5.4 4.7 1.6 7-6.2-3.8-6.2 3.8 1.6-7L2 9.5l7.1-.6z"/></svg>
      <svg viewBox="0 0 24 24"><path d="M12 2l2.9 6.9 7.1.6-5.4 4.7 1.6 7-6.2-3.8-6.2 3.8 1.6-7L2 9.5l7.1-.6z"/></svg>
      <svg viewBox="0 0 24 24"><path d="M12 2l2.9 6.9 7.1.6-5.4 4.7 1.6 7-6.2-3.8-6.2 3.8 1.6-7L2 9.5l7.1-.6z"/></svg>
      <svg viewBox="0 0 24 24"><path d="M12 2l2.9 6.9 7.1.6-5.4 4.7 1.6 7-6.2-3.8-6.2 3.8 1.6-7L2 9.5l7.1-.6z"/></svg>
      <svg viewBox="0 0 24 24"><path d="M12 2l2.9 6.9 7.1.6-5.4 4.7 1.6 7-6.2-3.8-6.2 3.8 1.6-7L2 9.5l7.1-.6z"/></svg>
    </div>
    <div class="listing-photo" role="img" aria-label="Profile photo of the advertiser"></div>
    <div class="listing-info">
      <h2 class="listing-name">Elina, 22</h2>
      <p class="listing-area">Birmingham City Centre Escort</p>
      <p class="listing-text">New to Birmingham - Hello guys, my name is Elina, I am from Sweden. My pictures are 100% genuine, I am a glamour model. Call me Kisses Elina xxx xxx I am a deep throat expert x OWO+CIM</p>
    </div>
  </section>

  <a class="cta cta-browse" href="#"><strong>Take a look:</strong><span>www.velvetlistings-uk.com</span></a>
  <a class="cta cta-post" href="#"><strong>Post an Ad:</strong><span>www.velvetlistings-uk.com/post/add</span></a>

  <footer class="footer">Try view on your <a href="#">Browser</a> or <a href="#">Unsubscribe</a></footer>
</main>
</body>
</html>
```